Innovation Company Business Card Design

I need to have my business card updated. The current card was designed when the company started 2.5 years ago and was a quick and dirty job.

I need a new card design that is more professional and has my updated company tag line.

I will include the old card's Corel Draw file, and EPS versions as examples of the current design. I will also include the company logo eps and corel version files.

The company pantone colour is pantone 1805 c (a dark red)

I want the design to convey the nature of our business as a strategic technology innovation company, but yet still be professional. We are funky vibey and work from an industrial style office in a vibey designer dominat part of town. Though are clients include large banks and corporate clients too.

The information that needs to be on the card is in attached word document (but doesn't have to be in this order or format)

Final version needs to be supplied in PNG preview, as well as PSD file format (or other editable file version) so that personal information on card can be easily edited and reprinted.

Target Market(s)

CEO's of small to medium size companies
Marketing Managers of large coporates
Account managers of Digital Agencies

Industry/Entity Type

Business

Requirements
Must have
• 86x54mm will be cut in rounded corner credit card size format (Except if you recommend otherwise in your design)
Nice to have
• Some kind of background transparency combined with the pantone colour that gives the card some dimension and depth. But no gradient fills please :-)
Should not have
• Basic gradient fills
• Clipart

```html
<!DOCTYPE html>
<html lang="en">
<head>
<meta charset="utf-8">
<title>Velantor Business Card</title>
<link rel="stylesheet" href="https://fonts.googleapis.com/css2?family=Arimo:wght@400;700&display=swap">
<style>
  :root {
    --brand-red: #b01f2e;
    --ink: #2b2b2b;
    --paper: #f7f7f5;
    --stage: #e6e4df;
    --white: #ffffff;
  }
  * { box-sizing: border-box; margin: 0; padding: 0; }
  html, body {
    width: 1200px; height: 1023px; overflow: hidden;
    background: var(--stage);
    font-family: "Arimo", Arial, sans-serif;
  }
  .canvas { position: relative; width: 1200px; height: 1023px; }

  /* Front card (portrait) */
  .card-front {
    position: absolute; left: 90px; top: 240px;
    width: 340px; height: 544px;
    background: var(--paper);
    border-radius: 26px;
    overflow: hidden;
    box-shadow: 0 6px 18px rgba(0,0,0,.12);
  }
  .front-accent {
    position: absolute; left: 0; top: 26px;
    width: 12px; height: 72px;
    background: var(--brand-red);
  }
  .contact-block { position: absolute; left: 32px; top: 26px; }
  .person-name { color: var(--brand-red); font-weight: 700; font-size: 23px; }
  .person-role { color: var(--ink); font-size: 15px; margin-top: 3px; }
  .contact-line { color: var(--ink); font-size: 15px; margin-top: 4px; }
  .contact-line:first-of-type { margin-top: 18px; }
  .contact-label { color: var(--brand-red); }

  .front-brand {
    position: absolute; left: 0; right: 0; top: 214px;
    text-align: center;
  }
  .brand-name {
    display: inline-block;
    color: var(--brand-red);
    font-weight: 700; font-size: 60px; letter-spacing: -1px;
    line-height: 1;
  }

  .company-block {
    position: absolute; right: 30px; top: 370px;
    text-align: right; font-size: 15px; line-height: 1.4; color: var(--ink);
    font-style: normal;
  }
  .company-name { color: var(--brand-red); }
  .front-wave { position: absolute; left: 0; bottom: 0; width: 340px; height: 80px; }

  /* Back card (landscape) */
  .card-back {
    position: absolute; left: 500px; top: 342px;
    width: 544px; height: 340px;
    background: var(--brand-red);
    border-radius: 26px;
    overflow: hidden;
    box-shadow: 0 6px 18px rgba(0,0,0,.15);
  }
  .back-panel {
    position: absolute; left: 70px; top: -40px;
    width: 300px; height: 300px;
    background: rgba(255,255,255,.07);
  }
  .back-panel-deep {
    position: absolute; left: 0; top: 0; width: 120px; height: 340px;
    background: rgba(0,0,0,.06);
  }
  .back-brand { position: absolute; left: 0; right: 0; top: 128px; text-align: center; }
  .back-brand .brand-name { color: var(--white); font-size: 76px; }
  .website {
    position: absolute; left: 40px; bottom: 32px;
    color: var(--white); font-weight: 700; font-size: 13px;
  }
</style>
</head>
<body>
<main class="canvas">
  <section class="card-front" aria-label="Business card front">
    <div class="front-accent"></div>
    <div class="contact-block">
      <p class="person-name">Daniel Marsh</p>
      <p class="person-role">Founder &amp; MD</p>
      <p class="contact-line"><span class="contact-label">E.</span> daniel@velantor.com</p>
      <p class="contact-line"><span class="contact-label">M.</span> 082 555 0147</p>
    </div>
    <div class="front-brand">
      <span class="brand-name">Velantor</span>
    </div>
    <address class="company-block">
      <span class="company-name">Velantor (Pty) Ltd</span><br>
      Suite 204, 18 Maple Ave.<br>
      Parkview, JHB, RSA<br>
      <span class="contact-label">P.</span> 010 555 0192
    </address>
    <svg class="front-wave" viewBox="0 0 340 80" preserveAspectRatio="none" aria-hidden="true">
      <path d="M0 18 C 110 40, 230 62, 340 70 L340 80 L0 80 Z" fill="var(--brand-red)"/>
      <path d="M0 8 C 110 30, 230 52, 340 60" fill="none" stroke="var(--brand-red)" stroke-width="3"/>
    </svg>
  </section>

  <section class="card-back" aria-label="Business card back">
    <div class="back-panel-deep"></div>
    <div class="back-panel"></div>
    <div class="back-brand">
      <span class="brand-name">Velantor</span>
    </div>
    <p class="website">www.velantor.com</p>
  </section>
</main>
</body>
</html>
```